Brightwater Facility Partners Business card

We wish to have a professional Business card to present to large Corporate CEO's ASAP.

Our web site helps explain our business www.brightwaterfp.org

Brightwater Facility Partners was established after we discovered how difficult it is to organise outsourced services while heading up a business or company.

We act as a facilitator for businesses who don't have the desire, expertise or recourses to manage their own systems and meet all their requirements.

We provide an all in one facility management solution for all types of businesses. We manage schedules, contractors and costs on behalf of businesses and their needs and wants.

Having an extensive network ensures we are able to connect businesses with the right service providers.

Target Market(s)

Company CEO

Industry/Entity Type

Business

Font styles to use
Sans Serif

Colors
33a6d7
f9fdfe
0355a3

Requirements
Must have
• professional design
Nice to have
• colours to match logo

```html
<!DOCTYPE html>
<html lang="en">
<head>
<meta charset="utf-8">
<title>Brightwater Facility Partners – Business Card</title>
<link href="https://fonts.googleapis.com/css2?family=Montserrat:wght@500;600;700&display=swap" rel="stylesheet">
<style>
  :root {
    --blue-light: #33a6d7;
    --blue-deep: #0355a3;
    --white: #f9fdfe;
    --stage: #e9edf1;
    --text-dark: #1d2a38;
  }
  * { margin: 0; padding: 0; box-sizing: border-box; }
  html, body {
    width: 1200px;
    height: 1000px;
    overflow: hidden;
    background: var(--stage);
    font-family: "Montserrat", Arial, sans-serif;
  }
  .card {
    position: absolute;
    left: 210px;
    width: 780px;
    height: 446px;
    overflow: hidden;
    box-shadow: 0 10px 30px rgba(0, 0, 0, 0.18);
    background: radial-gradient(ellipse at 55% 40%, var(--blue-light) 0%, #1b7fc3 45%, var(--blue-deep) 100%);
  }
  .card--back { top: 40px; }
  .card--front { top: 514px; }

  /* Back: centred brand */
  .brand {
    position: absolute;
    display: flex;
    align-items: center;
    gap: 16px;
    white-space: nowrap;
  }
  .brand__dot {
    border-radius: 50%;
    flex: none;
  }
  .brand__name {
    font-weight: 700;
    letter-spacing: 0.04em;
    text-transform: uppercase;
  }
  .card--back .brand {
    left: 50%;
    top: 50%;
    transform: translate(-50%, -50%);
  }
  .card--back .brand__dot {
    width: 44px; height: 44px;
    background: var(--white);
    opacity: 0.85;
  }
  .card--back .brand__name {
    font-size: 28px;
    color: var(--white);
  }

  /* Front: name, divider bar, contacts, footer band */
  .footer-band {
    position: absolute;
    left: 0; right: 0; bottom: 0;
    height: 96px;
    background: var(--white);
  }
  .divider-bar {
    position: absolute;
    left: 450px;
    top: 28px;
    width: 30px;
    height: 330px;
    background: var(--white);
  }
  .holder-name {
    position: absolute;
    right: 350px;
    top: 222px;
    font-size: 27px;
    font-weight: 700;
    letter-spacing: 0.05em;
    color: var(--white);
    text-transform: uppercase;
    white-space: nowrap;
  }
  .contact-list {
    position: absolute;
    left: 450px;
    top: 196px;
    list-style: none;
  }
  .contact-list li {
    display: flex;
    align-items: center;
    height: 36px;
  }
  .contact-list svg {
    width: 30px;
    height: 20px;
    flex: none;
  }
  .contact-list span {
    margin-left: 14px;
    font-size: 20px;
    font-weight: 500;
    color: var(--white);
  }
  .card--front .brand {
    right: 36px;
    bottom: 30px;
    gap: 12px;
  }
  .card--front .brand__dot {
    width: 30px; height: 30px;
    background: var(--blue-deep);
  }
  .card--front .brand__name {
    font-size: 18px;
    color: var(--blue-deep);
  }
</style>
</head>
<body>

  <section class="card card--back" aria-label="Business card back">
    <div class="brand">
      <span class="brand__dot"></span>
      <span class="brand__name">Brightwater Facility Partners</span>
    </div>
  </section>

  <section class="card card--front" aria-label="Business card front">
    <div class="footer-band"></div>
    <div class="divider-bar"></div>

    <h1 class="holder-name">Marcus Ellery</h1>

    <ul class="contact-list">
      <li>
        <svg viewBox="0 0 30 20" aria-hidden="true">
          <path d="M10 3c1 0 2 2.5 2 3.5s-1.5 1.2-1.2 2.2c.6 1.6 1.8 2.8 3.4 3.4 1 .3 1.2-1.2 2.2-1.2s3.5 1 3.5 2-1.2 3.3-3 3.3C11 16.2 6.8 12 6.8 6 6.8 4.2 9 3 10 3z" fill="#0355a3"/>
        </svg>
        <span>0412 555 208</span>
      </li>
      <li>
        <svg viewBox="0 0 30 20" aria-hidden="true">
          <rect x="6" y="4" width="18" height="12" fill="none" stroke="#0355a3" stroke-width="1.5"/>
          <path d="M6 4l9 7 9-7" fill="none" stroke="#0355a3" stroke-width="1.5"/>
        </svg>
        <span>marcus@brightwaterfp.org</span>
      </li>
      <li>
        <svg viewBox="0 0 30 20" aria-hidden="true">
          <circle cx="15" cy="10" r="8" fill="#1b7fc3"/>
          <path d="M9 7h12M8 12h14M15 2c-3 3-3 13 0 16M15 2c3 3 3 13 0 16" fill="none" stroke="#f9fdfe" stroke-width="1"/>
        </svg>
        <span>www.brightwaterfp.org</span>
      </li>
    </ul>

    <div class="brand">
      <span class="brand__dot"></span>
      <span class="brand__name">Brightwater Facility Partners</span>
    </div>
  </section>

</body>
</html>
```